professional business card design

Business card design. Photos have been uploaded and i am open to the designer choosing which photos to use. Would like the card to be mostyly in a grey scale design with black, whites, silver & grey colours. I have added copy of our flyer as would like on the back side of card our services to be listed. Do not use any bright colurs such as blue red green or yellow. i need to be able to edit the phone number and naem in the final card design submitted.

Target Market(s)

Clients

Industry/Entity Type

earhmovibng and transport

Contact Information for Business Card

Director Name, address, email, phone number and services

Colors

Designer to choose only greyscale colors for use in the design.

Requirements
Should not have
• no yellow, red, blue or green

```html
<!DOCTYPE html>
<html lang="en">
<head>
<meta charset="utf-8">
<title>Ridgeway Haulage – Business Card</title>
<link href="https://fonts.googleapis.com/css2?family=Archivo+Black&family=Roboto:ital,wght@0,400;0,700;1,400&display=swap" rel="stylesheet">
<style>
  :root {
    --stage: #d4d4d4;
    --black: #0b0b0b;
    --ink: #141414;
    --charcoal: #2a2a2a;
    --graphite: #444;
    --silver-light: #f1f1f1;
    --silver: #c9c9c9;
    --silver-dark: #9a9a9a;
    --white: #ffffff;
  }
  * { box-sizing: border-box; margin: 0; padding: 0; }
  html, body { width: 1200px; height: 800px; overflow: hidden; }
  body {
    background: var(--stage);
    font-family: "Roboto", Arial, sans-serif;
    position: relative;
  }
  .card {
    position: absolute;
    top: 245px;
    width: 540px;
    height: 310px;
    background: var(--black);
    overflow: hidden;
    box-shadow: 0 10px 26px rgba(0,0,0,.35);
  }
  .card--front { left: 40px; }
  .card--back { left: 620px; }

  .silver-band {
    position: absolute; left: 0; right: 0;
    background: linear-gradient(90deg, var(--silver-dark) 0%, var(--silver-light) 30%, var(--silver) 60%, var(--silver-light) 85%, var(--silver-dark) 100%);
  }
  .brand-name {
    position: absolute;
    font-family: "Roboto", Arial, sans-serif;
    font-weight: 700;
    color: var(--silver-light);
    letter-spacing: 2px;
    text-transform: uppercase;
    display: flex; align-items: center; gap: 10px;
  }
  .brand-name .brand-dot {
    width: 14px; height: 14px; border-radius: 50%;
    background: var(--silver);
  }

  /* Front */
  .front-hero {
    position: absolute; left: 0; top: 0; width: 540px; height: 170px;
    background: radial-gradient(ellipse at 30% 40%, #3a3a3a 0%, #161616 60%, #0b0b0b 100%);
  }
  .front-photo {
    position: absolute; left: 250px; top: 0; width: 290px; height: 170px;
    background: linear-gradient(100deg, rgba(60,60,60,0) 0%, #555 30%, #8a8a8a 60%, #5e5e5e 100%);
  }
  .card--front .brand-name { left: 30px; top: 62px; font-size: 24px; }
  .front-contact {
    position: absolute; left: 0; top: 170px; width: 540px; height: 60px;
    display: flex; align-items: center; padding: 0 26px;
    color: var(--white);
  }
  .person-name { font-weight: 700; font-size: 20px; letter-spacing: 1px; text-transform: uppercase; }
  .person-role { font-size: 12px; letter-spacing: 2px; text-transform: uppercase; text-align: right; color: var(--silver); }
  .divider { width: 1px; height: 38px; background: var(--graphite); margin: 0 22px; }
  .links { font-size: 12.5px; letter-spacing: .5px; line-height: 1.6; text-transform: uppercase; }
  .links li { list-style: none; display: flex; align-items: center; gap: 8px; }
  .links svg { width: 14px; height: 14px; }
  .phone-band { top: 230px; height: 38px; display: flex; align-items: center; padding-left: 26px; gap: 10px; }
  .phone-number { font-weight: 700; font-size: 21px; letter-spacing: 2px; color: var(--ink); }
  .address { position: absolute; left: 26px; top: 278px; font-size: 13px; color: var(--white); letter-spacing: .8px; text-transform: uppercase; }

  /* Back */
  .back-hero {
    position: absolute; left: 0; top: 0; width: 540px; height: 100px;
    background: radial-gradient(ellipse at 50% 40%, #3c3c3c 0%, #181818 60%, #0b0b0b 100%);
  }
  .card--back .brand-name { left: 0; right: 0; top: 34px; justify-content: center; font-size: 26px; }
  .services-band { top: 100px; height: 30px; display: flex; align-items: center; justify-content: center; }
  .services-title { font-family: "Archivo Black", Arial, sans-serif; font-size: 19px; letter-spacing: 3px; color: var(--ink); text-transform: uppercase; }
  .service-columns {
    position: absolute; left: 34px; right: 20px; top: 139px;
    display: grid; grid-template-columns: 1.05fr 1fr; gap: 14px;
    color: var(--white); font-size: 12.5px; line-height: 1.38;
  }
  .service-columns ul { list-style: none; }
  .service-columns li { position: relative; padding-left: 13px; }
  .service-columns li::before { content: ""; position: absolute; left: 0; top: 6px; width: 5px; height: 5px; border-radius: 50%; background: var(--white); }
  .quote-band { top: 256px; height: 54px; text-align: center; padding-top: 8px; }
  .quote-lead { font-style: italic; font-size: 11.5px; color: var(--charcoal); }
  .quote-call { font-weight: 700; font-size: 15.5px; color: var(--ink); margin-top: 2px; }
</style>
</head>
<body>
  <section class="card card--front" aria-label="Business card front">
    <div class="front-hero" role="img" aria-label="Dark perforated metal texture background"></div>
    <div class="front-photo" role="img" aria-label="Greyscale photo of a road train truck on a dirt road"></div>
    <div class="brand-name"><span class="brand-dot"></span>Ridgeway Haulage</div>

    <div class="front-contact">
      <div>
        <div class="person-name">Marcus Hale</div>
        <div class="person-role">Director</div>
      </div>
      <div class="divider"></div>
      <ul class="links">
        <li>
          <svg viewBox="0 0 16 16"><rect x="1" y="3" width="14" height="10" fill="#fff"/><path d="M1 3 L8 9 L15 3" fill="none" stroke="#0b0b0b" stroke-width="1.3"/></svg>
          hello@ridgewayhaul.com
        </li>
        <li>
          <svg viewBox="0 0 16 16"><circle cx="8" cy="8" r="7" fill="#fff"/><g fill="none" stroke="#0b0b0b" stroke-width="1"><ellipse cx="8" cy="8" rx="3" ry="7"/><line x1="1" y1="8" x2="15" y2="8"/></g></svg>
          www.ridgewayhaul.com
        </li>
      </ul>
    </div>

    <div class="silver-band phone-band">
      <svg width="18" height="18" viewBox="0 0 24 24"><circle cx="12" cy="12" r="11" fill="none" stroke="#141414" stroke-width="2"/><path d="M8 6.5c-1 1-1 3 1 6s4.5 4.5 6 4.5l1.5-1.5-2.3-2-1.2 1c-1-.5-2.5-2-3-3l1-1.2-2-2.3z" fill="#141414"/></svg>
      <span class="phone-number">061 482 730 915</span>
    </div>
    <p class="address">17 Quarry Road, Red Flats, 60871</p>
  </section>

  <section class="card card--back" aria-label="Business card back">
    <div class="back-hero" role="img" aria-label="Dark perforated metal texture background"></div>
    <div class="brand-name"><span class="brand-dot"></span>Ridgeway Haulage</div>

    <div class="silver-band services-band">
      <h2 class="services-title">Our Services</h2>
    </div>

    <div class="service-columns">
      <ul>
        <li>Over Size Loads / Hot Shot Loads</li>
        <li>Heavy Vehicle Recovery Services</li>
        <li>Potable Water Deliveries</li>
        <li>Road Building / Maintenance</li>
        <li>Earthworks</li>
        <li>Sand &amp; Metal Supply &amp; Cartage</li>
      </ul>
      <ul>
        <li>Road Train Tippers</li>
        <li>Road Train Tankers</li>
        <li>Road Train Flat Tops</li>
        <li>Drop Deck Trailers</li>
        <li>Mine Site accredited equipment &amp; Operators</li>
      </ul>
    </div>

    <div class="silver-band quote-band">
      <p class="quote-lead">we offer a large range of services not listed so</p>
      <p class="quote-call">Call us today for a personalised quote to suit your needs.</p>
    </div>
  </section>
</body>
</html>
```